NEW Modern Sleek Business Card for VR Language Startup

Our startup is using VR to lead the next wave of world language education. We need a two-sided business card that introduces the larger organization (Quorvel Language Inc) and our contact info on one side and shows the product, Lumidrasca, on the other side.

Side 1 (contact info)= Quorvel Logo and Contact info (name, title, phone, email)

Side 2 (product)= Lumidrasc logo, text, and website
Text= Culturally Immersive Language Learning Games
Website= www.lumidrasc.example

Target Market(s)

Education, Technology

Contact Information for Business Card

Contact info will be updated upon approval of the design. For now, put this as a placeholder.

Perry Hollins
Founder & CEO
phollins@mailtrove.example
(555)-014-2736

Font styles to use
Other font styles liked:
• Gibson and Century Gothic are the brand fonts

Requirements
Nice to have
• I would love to see cohesion between the design and colors of the two logos. I have attached a few business card designs that I like, so you can get a feel for my preferred style.

```html
<!DOCTYPE html>
<html lang="en">
<head>
<meta charset="utf-8">
<title>Quorvel Language — Business Cards</title>
<link rel="stylesheet" href="https://fonts.googleapis.com/css2?family=Lato:wght@300;400;700&display=swap">
<style>
  :root {
    --bg: #e9e6e1;
    --card: #ffffff;
    --pink: #ec5a6a;
    --violet: #7d6bbd;
    --indigo: #5a62b3;
    --edge: #6a6cba;
    --sky: #5fc6de;
    --ink: #2c2c3a;
    --grey: #5b5b66;
    --shadow: rgba(40, 30, 20, 0.22);
  }
  * { margin: 0; padding: 0; box-sizing: border-box; }
  html, body { width: 1200px; height: 1023px; overflow: hidden; background: var(--bg); }
  .sheet {
    width: 1200px; height: 1023px;
    display: flex; flex-direction: column; align-items: center; justify-content: center;
    gap: 56px;
  }
  .card {
    position: relative;
    width: 640px; height: 366px;
    border-radius: 26px;
    background: var(--card);
    overflow: hidden;
    box-shadow: 0 3px 0 #dcdcdc, 0 6px 0 #cfcfcf, 0 14px 30px var(--shadow);
  }
  .card svg.art { position: absolute; inset: 0; width: 100%; height: 100%; }

  /* Contact side */
  .brand-mark {
    position: absolute; left: 420px; right: 24px; top: 120px;
    text-align: center;
  }
  .brand-name {
    font-family: "Lato", sans-serif; font-weight: 700;
    font-size: 38px; letter-spacing: 4px; color: var(--ink);
  }
  .contact { position: absolute; left: 48px; top: 150px; }
  .contact-name {
    font-family: "Lato", sans-serif; font-weight: 700;
    font-size: 34px; color: var(--pink); line-height: 1.05;
  }
  .contact-title {
    font-family: "Lato", sans-serif; font-weight: 300;
    font-size: 22px; color: var(--violet); margin-top: 2px;
  }
  .contact-list { list-style: none; margin-top: 30px; }
  .contact-list li {
    display: flex; align-items: center; gap: 16px;
    font-family: "Lato", sans-serif; font-size: 19px; color: var(--grey);
    margin-bottom: 10px;
  }
  .contact-list svg { width: 20px; height: 20px; flex: none; }

  /* Product side */
  .product-mark {
    position: absolute; left: 0; right: 0; top: 72px;
    display: flex; align-items: center; justify-content: center; gap: 16px;
  }
  .product-dot { width: 50px; height: 50px; border-radius: 50%; background: var(--sky); }
  .product-name {
    font-family: "Lato", sans-serif; font-weight: 700;
    font-size: 50px; color: var(--indigo);
  }
  .tagline {
    position: absolute; left: 0; right: 0; top: 168px; text-align: center;
    font-family: "Lato", sans-serif; font-size: 21px; color: var(--grey);
  }
  .website {
    position: absolute; left: 44px; bottom: 24px;
    font-family: "Lato", sans-serif; font-size: 20px; color: #ffffff;
  }
</style>
</head>
<body>
<main class="sheet">

  <section class="card card--contact" aria-label="Contact side">
    <svg class="art" viewBox="0 0 640 366" preserveAspectRatio="none" aria-hidden="true">
      <defs>
        <linearGradient id="contact-wash" x1="0" y1="0" x2="1" y2="1">
          <stop offset="0" stop-color="#ec5a6a"/>
          <stop offset="0.55" stop-color="#a07ab8"/>
          <stop offset="1" stop-color="#5a62b3"/>
        </linearGradient>
        <radialGradient id="contact-glow" cx="0.76" cy="0.42" r="0.42">
          <stop offset="0" stop-color="#ffffff" stop-opacity="0.85"/>
          <stop offset="1" stop-color="#ffffff" stop-opacity="0"/>
        </radialGradient>
        <linearGradient id="contact-swoosh" x1="0" y1="0" x2="0" y2="1">
          <stop offset="0" stop-color="#ec5a6a"/>
          <stop offset="1" stop-color="#f7a08a"/>
        </linearGradient>
      </defs>
      <path d="M290 0 H640 V366 H470 C420 250 380 120 290 0 Z" fill="url(#contact-wash)"/>
      <path d="M290 0 H640 V366 H470 C420 250 380 120 290 0 Z" fill="url(#contact-glow)"/>
      <path d="M262 0 C350 90 400 200 430 340 C390 200 330 90 262 0 Z" fill="url(#contact-swoosh)"/>
      <path d="M282 0 C370 100 415 210 432 345" fill="none" stroke="#ffffff" stroke-width="2.5"/>
    </svg>

    <div class="brand-mark">
      <span class="brand-name">Quorvel</span>
    </div>

    <div class="contact">
      <h1 class="contact-name">Perry Hollins</h1>
      <p class="contact-title">Founder &amp; CEO</p>
      <ul class="contact-list">
        <li>
          <svg viewBox="0 0 20 20"><path d="M5 2 L8 2 L9 6 L7 8 C8 10.5 9.5 12 12 13 L14 11 L18 12 L18 15 C18 16.5 17 17.5 15.5 17.5 C9 17 3 11 2.5 4.5 C2.5 3 3.5 2 5 2 Z" fill="var(--pink)"/></svg>
          (555)-014-2736
        </li>
        <li>
          <svg viewBox="0 0 20 20"><rect x="2" y="4" width="16" height="12" rx="1.5" fill="var(--pink)"/><path d="M2.5 5 L10 11 L17.5 5" fill="none" stroke="#fff" stroke-width="1.6"/></svg>
          phollins@mailtrove.example
        </li>
      </ul>
    </div>
  </section>

  <section class="card card--product" aria-label="Product side">
    <svg class="art" viewBox="0 0 640 366" preserveAspectRatio="none" aria-hidden="true">
      <defs>
        <linearGradient id="product-band" x1="0" y1="0" x2="1" y2="0">
          <stop offset="0" stop-color="#5a62b3"/>
          <stop offset="0.5" stop-color="#7fb0d8"/>
          <stop offset="1" stop-color="#5fc6de"/>
        </linearGradient>
      </defs>
      <path d="M0 266 C200 282 420 312 640 336 V366 H0 Z" fill="url(#product-band)"/>
      <path d="M0 254 C190 270 400 298 640 322" fill="none" stroke="#6a6cba" stroke-width="2.5"/>
      <path d="M0 260 C195 276 410 305 640 329" fill="none" stroke="#ffffff" stroke-width="2"/>
      <rect x="0" y="356" width="640" height="10" fill="#6a6cba"/>
    </svg>

    <div class="product-mark">
      <span class="product-dot"></span>
      <span class="product-name">Lumidrasc</span>
    </div>
    <p class="tagline">Culturally Immersive Language Learning Games</p>
    <p class="website">www.lumidrasc.example</p>
  </section>

</main>
</body>
</html>
```